Marrowfield Contracting Business Cards

Front of card:

Full Logo
Name
Address
Office Phone
Cell Phone
Email
Website

Back:
Logo Mark in background
List and markets and services performed

```html
<!DOCTYPE html>
<html lang="en">
<head>
<meta charset="utf-8">
<title>Marrowfield Contracting Business Cards</title>
<link rel="stylesheet" href="https://fonts.googleapis.com/css2?family=Michroma&family=Poppins:wght@400;500;600&display=swap">
<style>
  :root {
    --brand-red: #d92128;
    --ink-grey: #55585c;
    --paper: #ffffff;
    --backdrop: #e4e5e7;
    --heading-font: "Michroma", sans-serif;
    --body-font: "Poppins", sans-serif;
  }
  * { box-sizing: border-box; margin: 0; padding: 0; }
  html, body { width: 1200px; height: 800px; overflow: hidden; }
  body {
    background: var(--backdrop);
    font-family: var(--body-font);
    display: flex;
    align-items: center;
    justify-content: center;
    gap: 40px;
  }
  .card {
    position: relative;
    width: 540px;
    height: 309px;
    border-radius: 4px;
    overflow: hidden;
    box-shadow: 0 8px 24px rgba(0,0,0,0.12);
  }

  /* Back card */
  .card-back { background: var(--brand-red); color: var(--paper); }
  .back-content { position: absolute; left: 34px; top: 28px; width: 300px; }
  .section-title {
    font-family: var(--heading-font);
    font-size: 15px;
    letter-spacing: 0.5px;
    margin-bottom: 5px;
  }
  .section-list { list-style: none; font-size: 11px; line-height: 15px; margin-bottom: 12px; padding-left: 2px; }
  .section-text { font-size: 11px; line-height: 15px; width: 290px; }
  .back-brand {
    position: absolute; right: 30px; bottom: 40px;
    display: flex; align-items: center; gap: 10px;
  }

  /* Front card */
  .card-front { background: var(--paper); color: var(--ink-grey); }
  .person { position: absolute; left: 36px; top: 30px; }
  .person-name {
    font-family: var(--heading-font);
    color: var(--brand-red);
    font-size: 15px;
    letter-spacing: 0.5px;
  }
  .person-role { font-size: 12px; margin-top: 2px; }
  .contact-list { position: absolute; left: 36px; top: 100px; list-style: none; font-size: 12px; line-height: 19px; }
  .contact-list li { display: flex; align-items: center; gap: 8px; }
  .contact-list svg { width: 11px; height: 11px; fill: var(--brand-red); flex: none; }
  .address-band {
    position: absolute; left: 0; right: 0; bottom: 38px; height: 30px;
    background: var(--brand-red); color: var(--paper);
    display: flex; align-items: center; gap: 8px; padding-left: 36px;
    font-size: 12px;
  }
  .address-band svg { width: 11px; height: 11px; fill: var(--paper); }
  .band-dot {
    position: absolute; right: 26px; top: 3px;
    width: 24px; height: 24px; border-radius: 50%; background: var(--paper);
  }
  .front-brand {
    position: absolute; right: 28px; top: 108px;
    display: flex; align-items: center; gap: 10px;
  }

  /* Brand lockup */
  .brand-dot { width: 34px; height: 34px; border-radius: 50%; flex: none; }
  .brand-name { font-family: var(--body-font); font-weight: 600; font-size: 16px; line-height: 19px; text-align: left; }
  .card-back .brand-dot { background: var(--paper); }
  .card-back .brand-name { color: var(--paper); }
  .card-front .brand-dot { background: var(--brand-red); }
  .card-front .brand-name { color: var(--brand-red); }
</style>
</head>
<body>

  <section class="card card-back" aria-label="Card back">
    <div class="back-content">
      <h2 class="section-title">SERVICES LIST</h2>
      <ul class="section-list">
        <li>Concrete Structure</li>
        <li>Concrete Pavement</li>
        <li>Bridges</li>
        <li>Site Concrete</li>
      </ul>
      <h2 class="section-title">MARKETS</h2>
      <ul class="section-list">
        <li>Dummy Place 1</li>
        <li>Dummy Place 2</li>
        <li>Dummy Place 3</li>
        <li>Dummy Place 4</li>
      </ul>
      <h2 class="section-title">SERVICES PERFORMED</h2>
      <p class="section-text">Your Service details here Lorem Ipsum is simply dummy text of the printing and typesetting industry.</p>
    </div>
    <div class="back-brand">
      <span class="brand-dot"></span>
      <span class="brand-name">Marrowfield<br>Contracting LLC</span>
    </div>
  </section>

  <section class="card card-front" aria-label="Card front">
    <div class="person">
      <h1 class="person-name">DANA OKAFOR</h1>
      <p class="person-role">Director</p>
    </div>
    <ul class="contact-list">
      <li><svg viewBox="0 0 12 12"><path d="M3 0h6a1 1 0 0 1 1 1v10a1 1 0 0 1-1 1H3a1 1 0 0 1-1-1V1a1 1 0 0 1 1-1zm0 1.5v8h6v-8z"/></svg>300-555-0142</li>
      <li><svg viewBox="0 0 12 12"><path d="M1 4c0-2 2-3 5-3s5 1 5 3v1H8V4H4v1H1zm1 2h8l1 5H1z"/></svg>300-555-0142</li>
      <li><svg viewBox="0 0 12 12"><path d="M0 2h12v8H0zm1 1l5 3.5L11 3z"/></svg>info@marrowfieldcontracting.com</li>
      <li><svg viewBox="0 0 12 12"><path d="M6 0a6 6 0 1 1 0 12A6 6 0 0 1 6 0zm0 1.5a4.5 4.5 0 1 0 0 9 4.5 4.5 0 0 0 0-9zM3 5.5h6v1H3zM5.5 2h1v8h-1z"/></svg>www.marrowfieldcontracting.com</li>
    </ul>
    <div class="front-brand">
      <span class="brand-dot"></span>
      <span class="brand-name">Marrowfield<br>Contracting LLC</span>
    </div>
    <div class="address-band">
      <svg viewBox="0 0 12 12"><path d="M6 0a4 4 0 0 1 4 4c0 3-4 8-4 8S2 7 2 4a4 4 0 0 1 4-4zm0 2.5a1.5 1.5 0 1 0 0 3 1.5 1.5 0 0 0 0-3z"/></svg>
      <span>00 dummy city, dummy place 0000</span>
      <span class="band-dot"></span>
    </div>
  </section>

</body>
</html>
```